Outdoor mass notification company needing business card design.

Our company name is Harborline Signal Systems Inc located in Amory Mississippi and we sell and maintain "Corvath" Mass Notification Sirens in the US. Outdoor sirens notify people of certain severe dangers such as tornados, severe thunderstorms, flooding, hurricanes and tsunamis. We also serve the oil and gas refining industries to warn of Chemical releases, fires, and lightning alerts.

Contact Information for Business Card

Name, title, cell number, email address

Requirements
Nice to have
• The Corvath logo and also the Tallbrook logo.

```html
<!DOCTYPE html>
<html lang="en">
<head>
<meta charset="utf-8">
<title>Harborline Signal Systems — Business Card</title>
<link href="https://fonts.googleapis.com/css2?family=Alegreya:wght@400;700&display=swap" rel="stylesheet">
<style>
  :root {
    --navy: #34536f;
    --paper: #ffffff;
    --backdrop: #c9c9c9;
    --ink-light: #ffffff;
  }
  * { margin: 0; padding: 0; box-sizing: border-box; }
  html, body { width: 1200px; height: 1015px; overflow: hidden; }
  body {
    background: var(--backdrop);
    font-family: "Alegreya", Georgia, serif;
    position: relative;
  }
  .card {
    position: absolute;
    left: 250px;
    width: 700px;
    height: 400px;
    overflow: hidden;
    box-shadow: 0 6px 18px rgba(0,0,0,0.25);
  }
  .card-front { top: 60px; background: var(--navy); }
  .card-back { top: 555px; background: var(--paper); }

  .brand-name {
    position: absolute;
    left: 0; right: 0;
    text-align: center;
    font-weight: 700;
    text-transform: uppercase;
    letter-spacing: 1px;
    line-height: 1;
  }
  .brand-name span { display: block; }
  .card-front .brand-name { top: 150px; color: var(--ink-light); font-size: 46px; }
  .card-back .brand-name { top: 50px; color: var(--navy); font-size: 44px; }

  .back-bands { position: absolute; inset: 0; }

  .holder {
    position: absolute;
    left: 40px;
    top: 268px;
    color: var(--ink-light);
  }
  .holder-name { font-weight: 700; font-size: 21px; text-transform: uppercase; letter-spacing: 0.5px; }
  .holder-title { font-size: 18px; margin-top: -2px; }
  .contact-list { list-style: none; margin-top: 14px; font-size: 19px; }
  .contact-list li { display: flex; align-items: center; gap: 10px; line-height: 1.35; }
  .contact-list svg { width: 18px; height: 18px; flex: none; }

  .company-info {
    position: absolute;
    right: 36px;
    top: 178px;
    text-align: right;
    color: var(--ink-light);
    font-size: 18px;
    line-height: 1.35;
  }
</style>
</head>
<body>

<section class="card card-front" aria-label="Card front">
  <h1 class="brand-name"><span>Harborline</span><span>Signal Systems</span></h1>
</section>

<section class="card card-back" aria-label="Card back">
  <svg class="back-bands" viewBox="0 0 700 400" preserveAspectRatio="none" aria-hidden="true">
    <polygon points="0,255 330,255 330,160 700,160 700,400 0,400" fill="var(--navy)"/>
  </svg>

  <h2 class="brand-name"><span>Harborline</span><span>Signal Systems</span></h2>

  <div class="company-info">
    <p>www.harborlinesignal.com</p>
    <p>118, Mill Street, Amory MS</p>
    <p>38821,United States</p>
  </div>

  <div class="holder">
    <p class="holder-name">Daniel Reeves</p>
    <p class="holder-title">Managing Director</p>
    <ul class="contact-list">
      <li>
        <svg viewBox="0 0 24 24" aria-hidden="true"><path fill="#fff" d="M6.6 10.8a15.1 15.1 0 0 0 6.6 6.6l2.2-2.2a1 1 0 0 1 1-.25 11.4 11.4 0 0 0 3.6.57 1 1 0 0 1 1 1V20a1 1 0 0 1-1 1A17 17 0 0 1 3 4a1 1 0 0 1 1-1h3.5a1 1 0 0 1 1 1c0 1.25.2 2.45.57 3.57a1 1 0 0 1-.25 1z"/></svg>
        044-555 010 234
      </li>
      <li>
        <svg viewBox="0 0 24 24" aria-hidden="true"><path fill="#fff" d="M2 5h20v14H2z"/><path fill="none" stroke="#34536f" stroke-width="1.6" d="M2 5l10 8 10-8"/></svg>
        info@harborline.com
      </li>
    </ul>
  </div>
</section>

</body>
</html>
```